HollowPine Ventures Inc. Business Card Design

My business is custom renovations and homes.I would need to have a new business logo created to go along with my company name. The business card should be of a modern style as this is the market I am focused on. I would need my contact information and website posted on the card. I would also like to list a few of the tasks I conduct on the card (such as: Renovations, Additions, Repairs, New Homes, Design, Consultations). On the reverse of the card I currently have just my logo and my motto, "Shaping A Bold Path". However, I am open to completely changing everything as I am starting a new year and would like to excel further. Any new ideas and suggestions are always welcomed. Thank you.

Target Market(s)

Upscale residential and commercial renovations and builds

Industry/Entity Type

Business

Contact Information for Business Card

I would like the design to be able to be laser cut or burnt onto a wooden business card. I will be creating one option of cards for really loyal customers (wooden) and a second option for the everyday customer (paper).

Font styles to use
Other font styles liked:
• Calibri / anything of mordern taste

Colors
f37122
5c5c5c
474747
ffffff

Requirements
Must have
• I would like the colours of my business to be a sharp orange and grey. I believe this will symbolize a modern style. I am open to other suggestions if this is not suitable for the designers tastes. My contact info as follows:
• Will Marsh
• President
• HollowPine Ventures Inc.
• 555-214-3987
• will@hollowpineventures.example
• I would like my website (currently under construction) hollowpineventures.example on the card aswell.
Nice to have
• Along with a modern logo representing HollowPine, I would like something on the card besides the logo and contact information. Perhaps a small background design. I feel it may be nice to have my services listed on the card (in smaller font on the bottom) Renovations, Additions, Repairs, Design, Consultations.
Should not have
• The business card should not have too many different colors. Should not have rounded corners.

```html
<!DOCTYPE html>
<html lang="en">
<head>
<meta charset="utf-8">
<title>HollowPine Ventures Inc. Business Card</title>
<link rel="stylesheet" href="https://fonts.googleapis.com/css2?family=Open+Sans:wght@400;600;700&family=Arimo:wght@400;700&display=swap">
<style>
  :root {
    --card: #1f2a33;
    --orange: #f5921e;
    --white: #ffffff;
    --backdrop: #e9e6e3;
  }
  * { margin: 0; padding: 0; box-sizing: border-box; }
  html, body { width: 1200px; height: 900px; overflow: hidden; }
  body {
    position: relative;
    background: var(--backdrop);
    font-family: "Open Sans", "Segoe UI", sans-serif;
    color: var(--white);
  }
  .card {
    position: absolute;
    width: 556px;
    height: 342px;
    background: var(--card);
  }
  .card--front { left: 238px; top: 62px; }
  .card--back { left: 459px; top: 518px; }

  /* Front */
  .brand-name {
    position: absolute;
    left: 58px; top: 108px;
    display: flex; align-items: center; gap: 10px;
    font-weight: 700; font-size: 30px;
    color: var(--orange);
  }
  .brand-square { width: 18px; height: 18px; background: var(--orange); }
  .holder { position: absolute; left: 284px; top: 88px; }
  .holder-name { font-weight: 700; font-size: 17px; color: var(--orange); line-height: 1.2; }
  .holder-role { font-size: 14px; line-height: 1.3; }
  .contact-list {
    position: absolute; left: 284px; top: 158px;
    list-style: none; font-size: 14.5px; line-height: 20px;
  }
  .contact-list li { display: flex; align-items: center; gap: 8px; }
  .contact-list svg { width: 12px; height: 12px; fill: var(--orange); flex: none; }
  .services {
    position: absolute; left: 0; right: 0; top: 268px;
    text-align: center; font-size: 14.5px;
  }

  /* Back */
  .back-mark {
    position: absolute; left: 248px; top: 80px;
    width: 60px; height: 60px; background: var(--orange);
  }
  .back-name {
    position: absolute; left: 0; right: 0; top: 168px;
    text-align: center;
    font-family: "Arimo", Arial, sans-serif;
  }
  .back-name-main { font-size: 38px; font-weight: 400; color: var(--orange); letter-spacing: 1px; line-height: 1; }
  .back-name-sub { font-size: 25px; letter-spacing: 2px; line-height: 1.2; }
  .motto {
    position: absolute; left: 0; right: 0; top: 266px;
    text-align: center; font-size: 21px; letter-spacing: 0.5px;
  }
</style>
</head>
<body>
  <section class="card card--front">
    <div class="brand-name"><span class="brand-square"></span>HollowPine</div>
    <div class="holder">
      <p class="holder-name">Will Marsh</p>
      <p class="holder-role">President</p>
    </div>
    <ul class="contact-list">
      <li><svg viewBox="0 0 24 24"><path d="M6.6 10.8a15 15 0 0 0 6.6 6.6l2.2-2.2c.3-.3.7-.4 1-.2 1.1.4 2.3.6 3.6.6.6 0 1 .4 1 1V20c0 .6-.4 1-1 1A17 17 0 0 1 3 4c0-.6.4-1 1-1h3.5c.6 0 1 .4 1 1 0 1.3.2 2.5.6 3.6.1.3 0 .7-.2 1z"/></svg>555-214-3987</li>
      <li><svg viewBox="0 0 24 24"><path d="M2 5h20v14H2z M3 6l9 7 9-7" stroke="#1f2a33" stroke-width="1.5"/></svg>will@hollowpineventures.example</li>
      <li><svg viewBox="0 0 24 24"><circle cx="12" cy="12" r="10"/></svg>www.hollowpineventures.example</li>
    </ul>
    <p class="services">Renovations | Additions | Repairs | New Homes | Design | Consultations</p>
  </section>

  <section class="card card--back">
    <div class="back-mark"></div>
    <div class="back-name">
      <p class="back-name-main">HOLLOWPINE</p>
      <p class="back-name-sub">Ventures Inc.</p>
    </div>
    <p class="motto">SHAPING A BOLD PATH</p>
  </section>
</body>
</html>
```